Brightwell Auto Care 4x9 Rack Card

Design a 4" wide by 9" tall rack card printed front and back using the copy, logo and images uploaded below. I am also uploading a current flyer so you can see the typestyles we use. I will get the exact name of the font for you ASAP. Also will be uploading some before and after pictures for the back of the rack card

Target Market(s)

Affluent consumers who need their car cleaned and detailed in a meticulous fashion

Requirements
Must have
• Under the logo, put the words...... Premium Steam Detailing & Ceramic Coating.........also put ther following wording on the front side: Get Steamed! We use steam to clean your vehicle helping save millions of gallons of water and protecting our rivers, streams and lakes from runoff.
Nice to have
• a screened back background of hexagons might be nice

```html
<!DOCTYPE html>
<html lang="en">
<head>
<meta charset="utf-8">
<title>Brightwell Auto Care – Rack Card</title>
<link href="https://fonts.googleapis.com/css2?family=Montserrat:ital,wght@0,400;0,600;0,700;0,800;1,400&family=Oswald:wght@500&family=Roboto:wght@300;400&family=Great+Vibes&display=swap" rel="stylesheet">
<style>
  :root {
    --backdrop: #9ac77f;
    --brand-blue: #4a82c6;
    --brand-blue-dark: #3f73b5;
    --brand-green: #6aaa4f;
    --paper: #ffffff;
    --screen-grey: #ececec;
    --ink: #333333;
    --photo-dark: #2b2f35;
    --photo-mid: #6d7580;
  }
  * { box-sizing: border-box; margin: 0; padding: 0; }
  html, body { width: 1200px; height: 1200px; overflow: hidden; }
  body { background: var(--backdrop); position: relative; font-family: "Montserrat", sans-serif; }

  .rack-card {
    position: absolute; top: 161px; width: 387px; height: 869px;
    background: var(--paper); overflow: hidden;
    box-shadow: 0 2px 6px rgba(0,0,0,.25);
  }
  .rack-card--front { left: 178px; }
  .rack-card--back  { left: 634px; background: linear-gradient(180deg, #fff 0%, #fff 28%, var(--screen-grey) 60%, var(--screen-grey) 100%); }

  .photo { position: absolute; background: linear-gradient(145deg, var(--photo-mid), var(--photo-dark)); }

  /* front */
  .hero-photo { left: 8px; top: 4px; width: 371px; height: 282px;
    background: radial-gradient(ellipse at 55% 45%, #c7ced6 0%, #7d8894 35%, #2a2e33 75%); }
  .brand-name { position: absolute; left: 0; right: 0; top: 318px; text-align: center;
    color: var(--brand-green); font-weight: 700; font-size: 33px; line-height: 1.08; letter-spacing: 2px; text-transform: uppercase; }
  .brand-rule { position: absolute; left: 48px; width: 291px; top: 426px; height: 2px; background: var(--brand-blue); }
  .tagline { position: absolute; left: 0; right: 0; top: 432px; text-align: center;
    font-family: "Oswald", sans-serif; font-weight: 500; font-size: 14px; color: var(--brand-green); letter-spacing: .2px; }
  .mission-box { position: absolute; left: 45px; top: 460px; width: 300px; height: 88px; border-radius: 9px;
    background: linear-gradient(180deg, #5a90d0, var(--brand-blue-dark)); color: #fff;
    font-family: "Roboto", sans-serif; font-weight: 300; font-size: 12.6px; line-height: 16.6px;
    text-align: center; padding: 10px 8px; }
  .locations { position: absolute; left: 45px; top: 567px; list-style: none;
    font-family: "Roboto", sans-serif; font-size: 13.4px; line-height: 17.5px; color: var(--ink); }
  .location { position: relative; padding-left: 19px; margin-bottom: 8px; }
  .location svg { position: absolute; left: 0; top: 1px; }
  .location::after { content: ""; position: absolute; left: 5px; top: 17px; bottom: -2px; width: 1px; background: #999; }
  .crew-photo { left: 242px; top: 565px; width: 145px; height: 168px;
    background: linear-gradient(135deg, #d7c8a4 0%, #3a4f8a 55%, #1f2430 100%); }
  .footer-wave { position: absolute; left: 0; top: 715px; }
  .footer-contact { position: absolute; left: 36px; top: 763px; color: #fff; }
  .footer-contact .lead { font-style: italic; font-size: 15px; text-decoration: underline; margin-bottom: 6px; }
  .footer-contact p { font-weight: 700; font-size: 16.5px; line-height: 21px; letter-spacing: .4px; }

  /* back */
  .shot-tag { position: absolute; background: var(--brand-blue); color: #fff; font-weight: 700;
    font-size: 10px; letter-spacing: 1px; display: flex; align-items: center; justify-content: center; }
  .shot-tag--vertical { writing-mode: vertical-rl; transform: rotate(180deg); }
  .shot-frame { position: absolute; border: 1px solid var(--brand-green); }
  .price-list { position: absolute; left: 20px; top: 297px; width: 350px; list-style: none; color: #fff; }
  .price-item { padding: 0 12px 0 24px; display: flex; flex-direction: column; justify-content: center;
    font-weight: 700; font-size: 15.5px; line-height: 21px; text-transform: uppercase; letter-spacing: .2px; }
  .price-item--blue { background: var(--brand-blue); }
  .price-item--green { background: var(--brand-green); }
  .slogan-script { position: absolute; left: 0; right: 0; top: 610px; text-align: center;
    font-family: "Great Vibes", cursive; font-size: 40px; color: var(--brand-blue); }
  .slogan-bold { position: absolute; left: 0; right: 0; top: 657px; text-align: center;
    font-weight: 800; font-size: 32px; color: var(--brand-green); }
  .quote-contact { position: absolute; left: 0; right: 0; top: 768px; text-align: center; color: #fff; }
  .quote-contact .lead { font-style: italic; font-size: 14.5px; }
  .quote-contact .phone { font-weight: 800; font-size: 34px; line-height: 40px; letter-spacing: 1px; }
  .quote-contact .web { font-size: 22px; line-height: 24px; }
</style>
</head>
<body>

<section class="rack-card rack-card--front" aria-label="Rack card front">
  <div class="photo hero-photo" role="img" aria-label="Hexagon collage of a detailer polishing the hood of a silver sports car"></div>

  <h1 class="brand-name">Brightwell<br>Auto Care</h1>
  <div class="brand-rule"></div>
  <p class="tagline">PREMIUM STEAM DETAILING &amp; CERAMIC COATING</p>

  <p class="mission-box">Get Steamed! We use steam to clean your vehicle helping save millions of gallons of water and protecting our rivers, streams and lakes from runoff.</p>

  <ul class="locations">
    <li class="location">
      <svg width="12" height="16" viewBox="0 0 12 16"><path d="M6 0a6 6 0 0 0-6 6c0 4.5 6 10 6 10s6-5.5 6-10a6 6 0 0 0-6-6z" fill="#4a82c6"/><circle cx="6" cy="6" r="2.3" fill="#fff"/></svg>
      1420 Larch Street @<br>The Larch Street Commons<br>Ridgeford
    </li>
    <li class="location">
      <svg width="12" height="16" viewBox="0 0 12 16"><path d="M6 0a6 6 0 0 0-6 6c0 4.5 6 10 6 10s6-5.5 6-10a6 6 0 0 0-6-6z" fill="#4a82c6"/><circle cx="6" cy="6" r="2.3" fill="#fff"/></svg>
      52 Aspenview Lane<br>Pine Hollow
    </li>
    <li class="location">
      <svg width="12" height="16" viewBox="0 0 12 16"><path d="M6 0a6 6 0 0 0-6 6c0 4.5 6 10 6 10s6-5.5 6-10a6 6 0 0 0-6-6z" fill="#4a82c6"/><circle cx="6" cy="6" r="2.3" fill="#fff"/></svg>
      390 Millbrook Rd #112<br>Elkvale
    </li>
  </ul>

  <div class="photo crew-photo" role="img" aria-label="Hexagon collage of a detailer steam cleaning a car"></div>

  <svg class="footer-wave" width="387" height="154" viewBox="0 0 387 154">
    <path d="M0 42 C90 12 240 38 387 4 L387 154 L0 154 Z" fill="#4a82c6"/>
    <path d="M0 36 C70 4 190 12 330 30" fill="none" stroke="#6aaa4f" stroke-width="5"/>
  </svg>
  <div class="footer-contact">
    <p class="lead">Call for information &amp; scheduling:</p>
    <p>Ridgeford&nbsp; (555) 410-2200</p>
    <p>Elkvale&nbsp; (555) 318-4471</p>
    <p>Pine Hollow (555) 262-7300</p>
  </div>
</section>

<section class="rack-card rack-card--back" aria-label="Rack card back">
  <div class="photo" style="left:19px;top:22px;width:157px;height:78px" role="img" aria-label="Engine bay before cleaning, covered in leaves"></div>
  <div class="shot-tag shot-tag--vertical" style="left:176px;top:22px;width:18px;height:78px">BEFORE</div>

  <div class="shot-frame" style="left:16px;top:110px;width:181px;height:85px"></div>
  <div class="photo" style="left:19px;top:113px;width:157px;height:79px" role="img" aria-label="Engine bay after steam cleaning"></div>
  <div class="shot-tag shot-tag--vertical" style="left:176px;top:113px;width:18px;height:79px">AFTER</div>

  <div class="photo" style="left:205px;top:22px;width:76px;height:171px" role="img" aria-label="Dashboard and console before detailing"></div>
  <div class="shot-tag" style="left:205px;top:176px;width:76px;height:17px">BEFORE</div>

  <div class="shot-frame" style="left:289px;top:19px;width:84px;height:177px"></div>
  <div class="photo" style="left:292px;top:22px;width:78px;height:171px" role="img" aria-label="Dashboard and console after detailing"></div>
  <div class="shot-tag" style="left:292px;top:176px;width:78px;height:17px">AFTER</div>

  <div class="photo" style="left:19px;top:205px;width:175px;height:78px" role="img" aria-label="Dirty car interior floor before detailing"></div>
  <div class="shot-tag" style="left:114px;top:265px;width:80px;height:18px;border-top-left-radius:14px">BEFORE</div>

  <div class="shot-frame" style="left:202px;top:202px;width:170px;height:83px"></div>
  <div class="photo" style="left:205px;top:205px;width:164px;height:77px" role="img" aria-label="Clean car interior after detailing"></div>
  <div class="shot-tag" style="left:205px;top:265px;width:80px;height:17px;border-top-right-radius:14px">AFTER</div>

  <ul class="price-list">
    <li class="price-item price-item--blue" style="height:65px">Premium Steam Washes<br>Starting at $100 &amp; Up</li>
    <li class="price-item price-item--green" style="height:67px">Full Steam Detailing<br>Starting at $275 &amp; Up</li>
    <li class="price-item price-item--blue" style="height:84px">Paint Correction<br>(Multi-Stage Polishing)<br>Starting at $650 &amp; Up</li>
    <li class="price-item price-item--green" style="height:44px">Headlight Restoration - $110</li>
    <li class="price-item price-item--blue" style="height:41px">Engine Steam Cleaning - $75</li>
  </ul>

  <p class="slogan-script">Fall In Love With</p>
  <p class="slogan-bold">YOUR CAR AGAIN!</p>

  <svg class="footer-wave" width="387" height="154" viewBox="0 0 387 154">
    <path d="M0 42 C90 12 240 38 387 4 L387 154 L0 154 Z" fill="#4a82c6"/>
    <path d="M0 36 C70 4 190 12 330 30" fill="none" stroke="#6aaa4f" stroke-width="5"/>
  </svg>
  <div class="quote-contact">
    <p class="lead">Ceramic Coating-Call or visit us for a Quote</p>
    <p class="phone">(555) 262-7300</p>
    <p class="web">www.brightwellautocare.com</p>
  </div>
</section>

</body>
</html>
```